Veterinary Practice

This is a large and small animal practice that primarily treats cattle,horses,dog and cats. I desire a business card with a picture of each of those animals. I prefer a black cow but the other animals can be any color. The back of the cards needs to have appointment scheduling information.

Industry/Entity Type

Business

Contact Information for Business Card

Copper Ridge Veterinary Services
Daniel M Petterby DVM
3847 S Highway 41
Ashford Bend KS 66190
785-312-9048

```html
<!DOCTYPE html>
<html lang="en">
<head>
<meta charset="utf-8">
<title>Copper Ridge Veterinary Services – Business Card</title>
<link rel="stylesheet" href="https://fonts.googleapis.com/css2?family=Roboto:wght@400;700&family=Roboto+Condensed:wght@400;700&display=swap">
<style>
  :root {
    --page-bg: #dcdcdc;
    --card-white: #ffffff;
    --brand-green: #1e7b3a;
    --text-grey: #555555;
    --rule-grey: #cfcfcf;
    --field-white: #ffffff;
  }
  * { box-sizing: border-box; margin: 0; padding: 0; }
  html, body { width: 885px; height: 1200px; overflow: hidden; }
  body {
    background: var(--page-bg);
    font-family: "Roboto", Arial, sans-serif;
    position: relative;
  }
  .card {
    position: absolute;
    left: 82px;
    width: 720px;
    height: 411px;
    box-shadow: 0 3px 10px rgba(0,0,0,0.18);
    overflow: hidden;
  }

  /* Front */
  .card-front { top: 150px; background: var(--card-white); }
  .brand {
    position: absolute; left: 44px; top: 48px;
    display: flex; align-items: flex-start; gap: 14px;
  }
  .brand-square {
    width: 54px; height: 54px; background: var(--brand-green); flex: none;
  }
  .brand-name {
    width: 200px;
    font-weight: 700; font-size: 24px; line-height: 1.15;
    color: var(--brand-green);
  }
  .contact {
    position: absolute; right: 44px; top: 200px;
    text-align: right; color: var(--text-grey);
  }
  .contact-name { font-size: 26px; margin-bottom: 14px; }
  .contact-rule {
    position: absolute; right: 44px; top: 244px;
    width: 330px; height: 1px; background: var(--rule-grey);
  }
  .contact-phone { font-size: 17px; margin-bottom: 6px; }
  .contact-address {
    font-size: 15px; display: flex; align-items: center; justify-content: flex-end; gap: 6px;
    white-space: nowrap;
  }
  .front-band {
    position: absolute; left: 0; right: 0; bottom: 0; height: 10px;
    background: var(--brand-green);
  }

  /* Back */
  .card-back {
    top: 640px; background: var(--brand-green);
    color: #ffffff;
    font-family: "Roboto Condensed", Arial, sans-serif;
  }
  .back-heading {
    position: absolute; left: 0; right: 0;
    text-align: center; font-size: 22px; letter-spacing: 1px;
  }
  .heading-appointment { top: 34px; }
  .back-rule {
    position: absolute; left: 44px; right: 44px; top: 70px;
    height: 2px; background: var(--field-white);
  }
  .day-row {
    position: absolute; left: 44px; right: 44px; top: 92px;
    display: flex; justify-content: space-between; align-items: center;
    font-size: 19px;
  }
  .day { display: flex; align-items: center; gap: 6px; }
  .check-box {
    width: 22px; height: 22px; background: var(--field-white); display: inline-block;
  }
  .time-row {
    position: absolute; left: 44px; right: 44px; top: 140px;
    display: flex; align-items: center; gap: 14px;
  }
  .time-field { flex: 1; height: 54px; background: var(--field-white); }
  .meridiem { display: flex; flex-direction: column; gap: 6px; font-size: 17px; }
  .meridiem span { display: flex; align-items: center; gap: 6px; }
  .meridiem .check-box { width: 18px; height: 18px; }
  .heading-questions { top: 218px; }
  .notes-field {
    position: absolute; left: 44px; right: 44px; top: 258px; height: 118px;
    background: var(--field-white);
  }
</style>
</head>
<body>

<section class="card card-front" aria-label="Business card front">
  <div class="brand">
    <span class="brand-square"></span>
    <span class="brand-name">Copper Ridge Veterinary Services</span>
  </div>
  <div class="contact">
    <p class="contact-name">Daniel M. Petterby</p>
    <p class="contact-phone">785-312-9048</p>
    <p class="contact-address">
      DVM 3847 S Highway 41 Ashford Bend KS 66190
      <svg width="14" height="18" viewBox="0 0 14 18" aria-hidden="true">
        <path d="M7 0C3.1 0 0 3 0 6.8 0 11.8 7 18 7 18s7-6.2 7-11.2C14 3 10.9 0 7 0zm0 9.4A2.6 2.6 0 1 1 7 4.2a2.6 2.6 0 0 1 0 5.2z" fill="#1e7b3a"/>
      </svg>
    </p>
  </div>
  <div class="contact-rule"></div>
  <div class="front-band"></div>
</section>

<section class="card card-back" aria-label="Business card back">
  <p class="back-heading heading-appointment">HAS AN APPOINTMENT ON</p>
  <div class="back-rule"></div>
  <div class="day-row">
    <span class="day"><span class="check-box"></span>MON</span>
    <span class="day"><span class="check-box"></span>TUES</span>
    <span class="day"><span class="check-box"></span>WED</span>
    <span class="day"><span class="check-box"></span>THURS</span>
    <span class="day"><span class="check-box"></span>FRI</span>
    <span class="day"><span class="check-box"></span>SAT</span>
  </div>
  <div class="time-row">
    <span class="time-field"></span>
    <span class="meridiem">
      <span><span class="check-box"></span>A.M.</span>
      <span><span class="check-box"></span>P.M.</span>
    </span>
  </div>
  <p class="back-heading heading-questions">THINGS TO ASK MY DENTIST</p>
  <div class="notes-field"></div>
</section>

</body>
</html>
```